Investment Funding, Building and Construction

I need a design logo for my new business based out of Houston, TX called Kestrel Ridge Holdings LLC., We are a company looking to help fund and invest into other small/businesses that do not want to deal with the banking system. We also remodel, renovate, and build from the ground up anything from residential, industrial warehousing, and commercial buildings. We would like the design to express our great deal of passion that we have for the work, our dedication to helping the costumer/businesses receive their expectation of work and also our professionalism and commitment to making sure we get the job done as perfect as possible. We want to build your future!

Target Market(s)

Architects, Design Companies, Home Owners and Real Estate

Industry/Entity Type

Construction Company

Contact Information for Business Card

Name: Dorian Pellham
Position: CEO/President
Company Name: Kestrel Ridge Holdings LLC.,
Website: www.kestrelridgehold.example
Phone: 281-507-3619
Email: kestrelridgehold@mailbox.example, crewfundflow@mailbox.example

Font styles to use
Serif

Colors
f04a50
3377b5

Requirements
Must have
• Motivational, Inspiring, and Detailed oriented work but simple.
Nice to have
• I would like to see excitement and enthusiasm within the card.
Should not have
• The project can not be boring and lack of detail.

```html
<!DOCTYPE html>
<html lang="en">
<head>
<meta charset="utf-8">
<title>Kestrel Ridge Holdings LLC – Business Card</title>
<link rel="stylesheet" href="https://fonts.googleapis.com/css2?family=Open+Sans:wght@400;700&family=Arimo:wght@400&display=swap">
<style>
  :root {
    --page-bg: #e6e7e9;
    --card-white: #f4f4f4;
    --brand-blue: #3377b5;
    --brand-red: #d95459;
    --brand-pink: #e3797c;
    --name-ink: #e9edf2;
    --contact-ink: #ffffff;
    --icon-teal: #4fc0b0;
    --logo-ink: #2e2e2e;
  }
  html, body {
    margin: 0;
    width: 1200px;
    height: 1200px;
    overflow: hidden;
    background: var(--page-bg);
  }
  .business-card {
    position: absolute;
    left: 75px;
    top: 300px;
    width: 1050px;
    height: 600px;
    background: var(--card-white);
    box-shadow: 0 14px 40px rgba(0, 0, 0, 0.18);
    overflow: hidden;
  }
  .card-art {
    position: absolute;
    inset: 0;
    width: 100%;
    height: 100%;
  }
  .holder {
    position: absolute;
    left: 100px;
    top: 128px;
    font-family: "Open Sans", sans-serif;
    color: var(--name-ink);
  }
  .holder-name {
    margin: 0;
    font-size: 38px;
    line-height: 1;
    font-weight: 400;
    letter-spacing: 0.3px;
    white-space: nowrap;
  }
  .holder-name .surname-first { font-weight: 700; }
  .holder-role {
    margin: 6px 0 0 20px;
    font-size: 18px;
    font-weight: 400;
    letter-spacing: 0.8px;
  }
  .contact-line {
    position: absolute;
    left: 180px;
    font-family: "Arimo", sans-serif;
    color: var(--contact-ink);
    font-size: 19px;
    line-height: 1.2;
    letter-spacing: 0.2px;
    white-space: nowrap;
  }
  .contact-phone { top: 249px; }
  .contact-email { top: 318px; }
  .contact-web { top: 409px; }
  .brand-block {
    position: absolute;
    left: 600px;
    width: 400px;
    top: 215px;
    text-align: center;
    font-family: "Arimo", sans-serif;
    color: var(--logo-ink);
  }
  .logo-slot {
    margin: 0;
    font-size: 32px;
    letter-spacing: -1px;
  }
  .company-name {
    margin: 30px 0 0;
    font-size: 30px;
    letter-spacing: -0.5px;
    font-weight: 400;
    white-space: nowrap;
  }
</style>
</head>
<body>
  <main class="business-card">
    <svg class="card-art" viewBox="0 0 1050 600" aria-hidden="true">
      <rect class="card-base" width="1050" height="600" fill="var(--card-white)"/>
      <path class="red-band" d="M230 0 H700 V600 H230 Z" fill="var(--brand-red)"/>
      <circle class="pink-band" cx="760" cy="260" r="380" fill="var(--brand-pink)"/>
      <rect class="right-white" x="780" y="0" width="270" height="600" fill="var(--card-white)"/>
      <circle class="white-disc" cx="780" cy="260" r="330" fill="var(--card-white)"/>
      <rect class="lower-white" x="700" y="430" width="350" height="170" fill="var(--card-white)"/>
      <path class="blue-field" d="M0 0 H250 C400 60 500 200 560 330 C610 440 660 540 710 600 H0 Z" fill="var(--brand-blue)"/>
      <g class="contact-icons" fill="none" stroke="var(--icon-teal)" stroke-width="2.5">
        <circle cx="140" cy="262" r="20"/>
        <path d="M133 253 c-3 2 -3 6 0 10 c3 5 7 8 11 8 c3 0 4 -2 4 -3 l-4 -3 l-3 2 c-2 -1 -5 -4 -6 -6 l2 -3 l-3 -4 z" fill="var(--icon-teal)" stroke="none"/>
        <circle cx="140" cy="340" r="20"/>
        <path d="M149 330 L130 342 L138 344 L140 352 Z" fill="var(--icon-teal)" stroke="none"/>
        <circle cx="140" cy="421" r="20"/>
        <g fill="var(--icon-teal)" stroke="none">
          <circle cx="133" cy="421" r="3.5"/>
          <circle cx="146" cy="414" r="3.5"/>
          <circle cx="146" cy="428" r="3.5"/>
        </g>
        <path d="M133 421 L146 414 M133 421 L146 428" stroke-width="2"/>
      </g>
    </svg>

    <div class="holder">
      <h1 class="holder-name"><span class="surname-first">DORIAN</span> Pellham</h1>
      <p class="holder-role">CEO/PRESIDENT</p>
    </div>

    <div class="contact-line contact-phone">+281-507-3619</div>
    <div class="contact-line contact-email">kestrelridgehold@mailbox.example<br>crewfundflow@mailbox.example</div>
    <div class="contact-line contact-web">www.kestrelridgehold.example</div>

    <div class="brand-block">
      <p class="logo-slot">LOGO HEAR</p>
      <h2 class="company-name">Kestrel Ridge Holdings LLC</h2>
    </div>
  </main>
</body>
</html>
```